High Quality Business card for Property Management Agency - Super Classy and professional design

High Quality Business card design.

We need a business card designed for our Property Management Agency.
We are located on Sydney's Northern Beaches and manage beautiful properties along the beach and harbor.
We need a design that oozes modern, classy and professional.
I would like it to be double sided with contact details and logo on the front and just the logo on the back.

I need a print ready PDF version of the file as well as an editable photoshop (PSD) version of the file.

Logo and information details attached.

Target Market(s)

Property owners/investors, Male and Female Aged 28-65

Industry/Entity Type

Real Estate

Contact Information for Business Card

Tom Carrick
Tel: 0467 239 018
Email: tom@harvestlaneestates.com.au
Website: www.harvestlaneestates.com.au
Address: Level 2, 17 Wattlecourt Rd, Dunmarra NSW 2187

Font styles to use
Sans Serif

Requirements
Must have
• - Logo front and back
• - Business card details listed above and attached
• - Colour
Nice to have
• Sleek and professional

```html
<!DOCTYPE html>
<html lang="en">
<head>
<meta charset="utf-8">
<title>Harvest Lane Estates – Business Card</title>
<link rel="stylesheet" href="https://fonts.googleapis.com/css2?family=Open+Sans:wght@400;600;700&display=swap">
<style>
  :root {
    --teal: #22a3b3;
    --teal-deep: #137a88;
    --ink: #15191c;
    --text: #2a2d30;
    --rule: #6f7377;
    --paper: #fbfbfb;
    --paper-shade: #e9eaeb;
    --backdrop: #d9d6d1;
  }
  * { box-sizing: border-box; margin: 0; padding: 0; }
  html, body { width: 1200px; height: 1023px; overflow: hidden; }
  body {
    background: var(--backdrop);
    font-family: "Open Sans", Arial, sans-serif;
    color: var(--text);
    display: flex;
    flex-direction: column;
    align-items: center;
    justify-content: center;
    gap: 44px;
  }
  .card {
    position: relative;
    width: 720px;
    height: 440px;
    border-radius: 22px;
    overflow: hidden;
    background: linear-gradient(135deg, var(--paper) 40%, var(--paper-shade) 100%);
    box-shadow: 0 6px 18px rgba(0,0,0,.18);
  }
  .band { position: absolute; display: block; }

  /* Front */
  .card--front .band { left: 0; bottom: 0; width: 720px; height: 26px; }
  .front-divider {
    position: absolute; left: 370px; top: 0; bottom: 26px;
    width: 1px; background: var(--rule);
  }
  .front-panel-left {
    position: absolute; left: 0; top: 0; width: 370px; bottom: 26px;
    display: flex; align-items: center; justify-content: center;
    padding-top: 40px;
  }
  .front-logo { display: flex; align-items: center; gap: 9px; }
  .logo-mark { width: 14px; height: 14px; background: var(--teal); flex: none; }
  .logo-name {
    font-weight: 600; font-size: 22px; color: var(--ink);
    text-transform: uppercase; letter-spacing: -0.4px; white-space: nowrap;
  }
  .holder {
    position: absolute; left: 420px; right: 0; top: 52px;
    display: flex; align-items: center; gap: 12px;
  }
  .holder-name { font-weight: 700; font-size: 32px; color: var(--teal); white-space: nowrap; }
  .holder-rule { flex: 1; height: 1px; background: var(--rule); }
  .contacts {
    position: absolute; right: 30px; top: 118px;
    list-style: none; text-align: right;
    font-size: 15px; line-height: 27px; color: var(--text);
  }
  .contacts li { display: flex; justify-content: flex-end; align-items: flex-start; gap: 10px; }
  .contacts svg { flex: none; margin-top: 5px; }

  /* Back */
  .card--back .band { left: 0; top: 0; width: 720px; height: 30px; }
  .back-site {
    position: absolute; left: 36px; top: 44px;
    font-size: 16px; letter-spacing: .3px; color: var(--text);
  }
  .back-logo {
    position: absolute; left: 0; right: 0; top: 205px;
    display: flex; justify-content: center; align-items: center; gap: 14px;
  }
  .back-logo .logo-mark { width: 26px; height: 26px; }
  .back-logo .logo-name { font-size: 46px; letter-spacing: -0.5px; }
</style>
</head>
<body>

<section class="card card--front">
  <div class="front-panel-left">
    <div class="front-logo">
      <span class="logo-mark"></span>
      <span class="logo-name">Harvest Lane Estates</span>
    </div>
  </div>
  <div class="front-divider"></div>

  <div class="holder">
    <span class="holder-name">Tom Carrick</span>
    <span class="holder-rule"></span>
  </div>

  <ul class="contacts">
    <li>0467 239 018
      <svg width="14" height="14" viewBox="0 0 24 24"><path fill="#22a3b3" d="M6.6 10.8a15.1 15.1 0 0 0 6.6 6.6l2.2-2.2c.3-.3.7-.4 1-.2 1.1.4 2.3.6 3.6.6.6 0 1 .4 1 1V20c0 .6-.4 1-1 1A17 17 0 0 1 3 4c0-.6.4-1 1-1h3.5c.6 0 1 .4 1 1 0 1.3.2 2.5.6 3.6.1.3 0 .7-.2 1z"/></svg></li>
    <li>tom@harvestlaneestates.com.au
      <svg width="15" height="14" viewBox="0 0 24 20"><rect x="1.5" y="2" width="21" height="16" fill="none" stroke="#22a3b3" stroke-width="2"/><path d="M1.5 3l10.5 8 10.5-8" fill="none" stroke="#22a3b3" stroke-width="2"/></svg></li>
    <li>www.harvestlaneestates.com.au
      <svg width="15" height="15" viewBox="0 0 24 24" fill="none" stroke="#22a3b3" stroke-width="2"><circle cx="12" cy="12" r="10"/><path d="M2 12h20M12 2c3 3 3 17 0 20M12 2c-3 3-3 17 0 20"/></svg></li>
    <li><span>Level 2, 17 Wattlecourt Rd,<br>Dunmarra NSW 2187</span>
      <svg width="13" height="16" viewBox="0 0 20 26"><path fill="#22a3b3" d="M10 0a9 9 0 0 0-9 9c0 7 9 17 9 17s9-10 9-17a9 9 0 0 0-9-9zm0 12.5A3.5 3.5 0 1 1 10 5.5a3.5 3.5 0 0 1 0 7z"/></svg></li>
  </ul>

  <svg class="band" viewBox="0 0 720 26" preserveAspectRatio="none" aria-hidden="true">
    <rect width="720" height="26" fill="var(--ink)"/>
    <polygon points="560,0 720,0 720,26 546,26" fill="var(--teal-deep)"/>
    <polygon points="546,26 560,0 566,0 552,26" fill="#e8e8e8"/>
  </svg>
</section>

<section class="card card--back">
  <svg class="band" viewBox="0 0 720 30" preserveAspectRatio="none" aria-hidden="true">
    <rect width="720" height="30" fill="var(--ink)"/>
    <polygon points="0,0 384,0 370,30 0,30" fill="var(--teal-deep)"/>
    <polygon points="384,0 390,0 376,30 370,30" fill="#e8e8e8"/>
  </svg>
  <p class="back-site">www.harvestlaneestates.com.au</p>
  <div class="back-logo">
    <span class="logo-mark"></span>
    <span class="logo-name">Harvest Lane Estates</span>
  </div>
</section>

</body>
</html>
```